Renewal of the Ferravolt SA Website

Ferravolt SA is a metal construction company active in industrial piping, boilermaking and metal framing. We would like to renew our site.

This website must be ready to work with Wordpress.

The site will contain the following pages: Home, skills, presentation, contact.

The site must reflect the field of the metal construction sector. It must be clear and easily understandable. The objective is not to win mandates with but to present the company and its capabilities.

I have inserted the pages of our old presentations, to describe our sector but we do not want to reuse these elements, we are waiting for your creativity to surprise us. In the 2nd phase we will complete with new images if necessary and texts

Target Market(s)

International companies in the food, chemical and pharmaceutical sectors

Industry/Entity Type

Alimentaire, pharma, chimie

Number of Pages Required

4 page

Font styles to use
Sans Serif

Colors
0054AA
0677BA
7BADD7
CADEEF
E8F1F8

Requirements
Must have
• It must contain at least the requested pages, images of illustrations, places for descriptions
Should not have
• Elements that appear or disappear, too flash,

```html
<!DOCTYPE html>
<html lang="fr">
<head>
<meta charset="utf-8">
<title>Ferravolt SA – Construction métallique</title>
<link href="https://fonts.googleapis.com/css2?family=Poppins:wght@300;400;500;600&family=Montserrat:wght@500;600&display=swap" rel="stylesheet">
<style>
:root{
  --blue:#1e4ba2;
  --blue-light:#7badd7;
  --ink:#1c1c1c;
  --text:#3a3a3a;
  --dark:#333333;
  --grey-bg:#f2f2f2;
  --footer:#111111;
  --white:#ffffff;
  --star:#f2a81d;
}
*{box-sizing:border-box;margin:0;padding:0}
html,body{width:1200px;height:3829px;overflow:hidden}
body{font-family:'Poppins',sans-serif;color:var(--text);background:var(--white);position:relative}
.abs{position:absolute}
.btn{position:absolute;display:flex;align-items:center;justify-content:center;background:var(--blue);color:var(--white);font-size:13px;font-weight:500;text-decoration:none}
/* header */
.site-header{position:absolute;left:0;top:0;width:1200px;height:75px;background:var(--white)}
.brand{position:absolute;left:141px;top:18px;font-size:28px;font-weight:600;color:var(--blue);letter-spacing:1px}
.nav a{position:absolute;top:27px;font-size:13px;color:var(--ink);text-decoration:none;font-weight:500}
.nav a.active{color:var(--blue)}
/* hero */
.hero{position:absolute;left:0;top:75px;width:1200px;height:602px;background:linear-gradient(180deg,#3a4a6e 0%,#4a4e5a 45%,#6a5a3a 80%,#3a3326 100%)}
.hero h1{position:absolute;left:140px;top:205px;width:920px;text-align:center;font-family:'Montserrat',sans-serif;font-weight:600;font-size:29px;line-height:39px;color:var(--white)}
.hero .btn{left:530px;top:340px;width:141px;height:37px;background:var(--white);color:var(--blue)}
/* about */
.about-photo{position:absolute;left:147px;top:745px;width:388px;height:544px;background:linear-gradient(160deg,#8a96a8,#4b5a74 55%,#2b3346)}
.about-frame-v{position:absolute;left:141px;top:766px;width:5px;height:528px;background:var(--blue)}
.about-frame-h{position:absolute;left:141px;top:1289px;width:283px;height:5px;background:var(--blue)}
.eyebrow{position:absolute;left:611px;top:754px;font-size:18px;color:var(--blue);display:flex;align-items:center;gap:10px}
.eyebrow::after{content:"";width:48px;height:2px;background:var(--blue)}
.about h2{position:absolute;left:611px;top:780px;font-size:29px;font-weight:500;color:var(--ink)}
.about-copy{position:absolute;left:611px;top:830px;width:448px;font-size:13px;line-height:21.5px}
.about-copy p{margin-bottom:16px}
.stats{position:absolute;left:422px;top:1224px;width:637px;height:97px;display:flex}
.stat{flex:1;padding:18px 12px;color:var(--white)}
.stat:nth-child(odd){background:var(--dark)}
.stat:nth-child(even){background:var(--blue)}
.stat b{display:block;font-size:26px;font-weight:500;line-height:30px}
.stat span{font-size:12px;line-height:15px;display:block}
/* skills */
.skills{position:absolute;left:0;top:1405px;width:1200px;height:699px;background:var(--grey-bg)}
.section-title{position:absolute;left:0;width:1200px;text-align:center;font-size:30px;font-weight:500;color:var(--ink)}
.skill-card{position:absolute;top:142px;width:291px;height:406px;color:var(--white);text-align:center}
.skill-card h3{position:absolute;left:0;width:100%;bottom:22px;font-size:18px;font-weight:500}
.skill-card.featured h3{bottom:auto;top:192px}
.skill-card p{position:absolute;left:28px;right:28px;top:225px;font-size:12px;line-height:19px}
/* vision */
.vm-box{position:absolute;left:141px;width:448px;height:180px;border:1px dashed #bdbdbd;padding:30px 34px}
.vm-box h3{display:flex;align-items:center;gap:12px;font-size:24px;font-weight:500;color:var(--ink)}
.vm-box p{margin-top:18px;font-size:13px;line-height:22px}
.vm-photo{position:absolute;left:617px;top:2189px;width:442px;height:372px;background:linear-gradient(160deg,#1d2a36,#3b3a34 50%,#8a5a2a 80%,#2a2520)}
.vm-frame-v{position:absolute;left:1060px;top:2216px;width:6px;height:352px;background:var(--blue)}
.vm-frame-h{position:absolute;left:739px;top:2562px;width:327px;height:6px;background:var(--blue)}
/* clients */
.clients{position:absolute;left:0;top:2650px;width:1200px;height:401px;background:linear-gradient(100deg,#1e1812 0%,#3b2614 45%,#6a3a14 75%,#b06418 100%)}
.clients .section-title{top:80px;color:var(--white)}
.clients .lead{position:absolute;left:0;width:1200px;top:140px;text-align:center;font-size:17px;font-weight:500;color:var(--white)}
.client-logo{position:absolute;top:200px;width:172px;height:113px;background:var(--white);display:flex;align-items:center;justify-content:center;gap:8px;font-size:26px;font-weight:500;color:var(--ink)}
.client-logo i{width:22px;height:22px;border-radius:50%;background:var(--blue)}
.arrow{position:absolute;width:40px;height:40px;border-radius:50%;background:var(--white);display:flex;align-items:center;justify-content:center}
.arrow.outline{background:transparent;border:1px solid var(--white)}
/* reviews */
.review{position:absolute;top:3204px;width:451px;height:250px;background:var(--white);box-shadow:0 2px 14px rgba(0,0,0,.08);text-align:center}
.review .quote{position:absolute;left:0;width:100%;top:20px;font-size:90px;line-height:90px;color:#e5e5e5;font-family:Georgia,serif}
.review p{position:absolute;left:36px;right:36px;top:92px;font-size:13px;line-height:22px;color:var(--text)}
.review h4{position:absolute;left:0;width:100%;top:190px;font-size:16px;font-weight:400;color:var(--ink)}
.review .stars{position:absolute;left:0;width:100%;top:214px;color:var(--star);font-size:11px;letter-spacing:1px}
.review::after{content:"";position:absolute;left:14px;right:14px;bottom:0;height:2px;background:var(--blue-light)}
/* footer */
.site-footer{position:absolute;left:0;top:3527px;width:1200px;height:302px;background:var(--footer);color:var(--white)}
.foot-brand{position:absolute;left:141px;top:70px;font-size:32px;font-weight:600;color:var(--white);letter-spacing:1px}
.social{position:absolute;top:142px;width:26px;height:26px;border-radius:50%;border:1px solid var(--white)}
.foot-h{position:absolute;top:37px;font-size:17px;font-weight:500}
.foot-links a{position:absolute;left:547px;font-size:13px;color:var(--white);text-decoration:none}
.foot-links a.active{text-decoration:underline}
.contact-item{position:absolute;left:830px;display:flex;gap:14px;font-size:13px;line-height:20px;align-items:flex-start}
.contact-item .ic{width:34px;height:34px;border-radius:50%;border:1px solid var(--white);flex:none;display:flex;align-items:center;justify-content:center}
.contact-item b{font-weight:600}
.foot-rule{position:absolute;left:141px;top:238px;width:918px;height:1px;background:#444}
.copyright{position:absolute;left:0;width:1200px;top:260px;text-align:center;font-size:12px}
</style>
</head>
<body>

<header class="site-header">
  <div class="brand">FERRAVOLT <span style="font-size:13px">SA</span></div>
  <nav class="nav">
    <a class="active" style="left:628px">Maison</a>
    <a style="left:698px">Compétences</a>
    <a style="left:813px">Présentation</a>
  </nav>
  <a class="btn" style="left:917px;top:18px;width:142px;height:38px">Contactez-nous</a>
</header>

<section class="hero" role="img" aria-label="Raffinerie industrielle au crépuscule, cheminées et tuyauteries">
  <h1>Ferravolt SA Est Une Entreprise De Construction Métallique Active Dans Les Domaines De La Tuyauterie Industrielle, De La Chaudronnerie Et De La Charpente Métallique.</h1>
  <a class="btn">Contactez-nous</a>
</section>

<section class="about">
  <div class="about-frame-v"></div>
  <div class="about-frame-h"></div>
  <div class="about-photo" role="img" aria-label="Deux ingénieurs en casque de chantier consultant un plan sur site"></div>
  <div class="eyebrow">À Propos De Nous</div>
  <h2>Ferravolt</h2>
  <div class="about-copy">
    <p>Lorem ipsum dolor sit amet, consectetur adipiscing elit. Fusce efficitur libero non ante luctus tincidunt. Curabitur commodo tortor purus, sit amet pellentesque odio mattis vel. Suspendisse sit amet magna sed dui dapibus tristique.</p>
    <p>Fusce egestas purus imperdiet, consequat diam ut, consequat nulla. Maecenas non felis pharetra, porta dolor nec, pulvinar dolor. Cras risus erat, iaculis vitae augue et, consequat luctus urna.</p>
    <p>Nullam eu sagittis urna, non rutrum tellus. Proin quis mi lectus. Curabitur id nulla non arcu auctor molestie. Nulla ipsum justo, pellentesque gravida bibendum nec, porta eu lectus. Phasellus ipsum justo, gravida non elementum id, dignissim ut diam. In hac habitasse platea dictumst.</p>
  </div>
  <a class="btn" style="left:611px;top:1140px;width:142px;height:38px">Contactez-nous</a>
  <div class="stats">
    <div class="stat"><b>150+</b><span>Projet Terminé</span></div>
    <div class="stat"><b>50+</b><span>Projet En Cours</span></div>
    <div class="stat"><b>45+</b><span>Équipe De<br>Compétences</span></div>
    <div class="stat"><b>200+</b><span>Équipe Non<br>Compétente</span></div>
  </div>
</section>

<section class="skills">
  <h2 class="section-title" style="top:80px">Nos Compétences</h2>
  <div class="skill-card" style="left:141px;background:linear-gradient(160deg,#c9ccd2,#7d8794 50%,#3c4350)" role="img" aria-label="Installation de tuyauterie industrielle en inox">
    <h3>Tuyauterie Industrielle</h3>
  </div>
  <div class="skill-card featured" style="left:454px;background:linear-gradient(180deg,#2b2d30,#141516)">
    <svg class="abs" style="left:105px;top:95px" width="82" height="80" viewBox="0 0 82 80" fill="none" stroke="#fff" stroke-width="2">
      <rect x="18" y="6" width="30" height="22"/><path d="M48 18h14v30"/><rect x="4" y="34" width="22" height="38"/><rect x="30" y="40" width="44" height="28"/><circle cx="62" cy="54" r="7"/><path d="M2 74h78"/>
    </svg>
    <h3>Chaudronnerie</h3>
    <p>Aliquam in dignissim leo. Fusce tempus, metus nec hendrerit vehicula, lacus sapien ornare arcu, et consequat odio massa sed purus.</p>
  </div>
  <div class="skill-card" style="left:767px;background:linear-gradient(160deg,#3a4a52,#2a2f30 50%,#6a5438)" role="img" aria-label="Charpente métallique d'un hall industriel">
    <h3>Charpente Métallique</h3>
  </div>
  <a class="btn" style="left:530px;top:577px;width:141px;height:37px">Contactez-nous</a>
</section>

<section class="vision">
  <div class="vm-box" style="top:2189px">
    <h3><svg width="44" height="44" viewBox="0 0 44 44" fill="none" stroke="#1e4ba2" stroke-width="2"><circle cx="22" cy="22" r="14"/><circle cx="22" cy="22" r="6"/><path d="M4 22c6-9 30-9 36 0c-6 9-30 9-36 0z"/></svg>Notre Vision</h3>
    <p>Aliquam in dignissim leo. Fusce tempus, metus nec hendr rit vehicula, lacus sapien ornare arcu, et consequat odio massa sed purus. Integer sagittis, leo ac.</p>
  </div>
  <div class="vm-box" style="top:2385px;padding-left:40px">
    <h3><svg width="46" height="46" viewBox="0 0 46 46" fill="none" stroke="#1e4ba2" stroke-width="2"><circle cx="22" cy="24" r="19"/><circle cx="22" cy="24" r="12"/><circle cx="22" cy="24" r="5"/><path d="M22 24L40 6M34 6h6v6"/></svg>Notre Mission</h3>
    <p>Aliquam in dignissim leo. Fusce tempus, metus nec hendr rit vehicula, lacus sapien ornare arcu, et consequat odio massa sed purus. Integer sagittis, leo ac.</p>
  </div>
  <div class="vm-frame-v"></div>
  <div class="vm-frame-h"></div>
  <div class="vm-photo" role="img" aria-label="Intérieur d'une aciérie avec poche de coulée suspendue"></div>
</section>

<section class="clients" role="img" aria-label="Fond d'atelier de fonderie aux tons orangés">
  <h2 class="section-title">Nos Clients</h2>
  <div class="lead">Aliquam in dignissim leo. Fusce tempus, metus nec hendr rit vehicula, lacus sapien ornare arcu.</div>
  <div class="arrow outline" style="left:78px;top:235px"><svg width="18" height="18" viewBox="0 0 18 18" fill="none" stroke="#fff" stroke-width="2"><path d="M15 9H3M8 4L3 9l5 5"/></svg></div>
  <div class="client-logo" style="left:141px"><i></i>Kelto</div>
  <div class="client-logo" style="left:327px"><i></i>Brinex</div>
  <div class="client-logo" style="left:514px"><i></i>Vardo</div>
  <div class="client-logo" style="left:700px"><i></i>Olmira</div>
  <div class="client-logo" style="left:887px"><i></i>Tessa</div>
  <div class="arrow" style="left:1081px;top:235px"><svg width="18" height="18" viewBox="0 0 18 18" fill="none" stroke="#1e4ba2" stroke-width="2"><path d="M3 9h12M10 4l5 5-5 5"/></svg></div>
</section>

<section class="reviews">
  <h2 class="section-title" style="top:3127px">Avis Clients Satisfaits</h2>
  <div class="arrow" style="left:78px;top:3308px;box-shadow:0 2px 10px rgba(0,0,0,.12)"><svg width="18" height="18" viewBox="0 0 18 18" fill="none" stroke="#1e4ba2" stroke-width="2"><path d="M15 9H3M8 4L3 9l5 5"/></svg></div>
  <div class="review" style="left:141px">
    <div class="quote">“”</div>
    <p>Quisque mollis consequat efficitur. Vestibulum ante ipsum aucibus orci luctus et ultrices posuere cubilia curae; Donec vitae dapibus dolor. Sed laoreet pulvinar felis, ut euismod ante gravidarisus, in rhoncus quam.</p>
    <h4>Clara Mendel</h4>
    <div class="stars">★★★★★</div>
  </div>
  <div class="review" style="left:608px">
    <div class="quote">“”</div>
    <p>Quisque mollis consequat efficitur. Vestibulum ante ipsum aucibus orci luctus et ultrices posuere cubilia curae; Donec vitae dapibus dolor. Sed laoreet pulvinar felis, ut euismod ante gravidarisus, in rhoncus quam.</p>
    <h4>Marc Delorme</h4>
    <div class="stars">★★★★★</div>
  </div>
  <div class="arrow" style="left:1081px;top:3308px;box-shadow:0 2px 10px rgba(0,0,0,.12)"><svg width="18" height="18" viewBox="0 0 18 18" fill="none" stroke="#1e4ba2" stroke-width="2"><path d="M3 9h12M10 4l5 5-5 5"/></svg></div>
</section>

<footer class="site-footer">
  <div class="foot-brand">FERRAVOLT <span style="font-size:14px">SA</span></div>
  <span class="social" style="left:215px"></span>
  <span class="social" style="left:252px"></span>
  <span class="social" style="left:289px"></span>
  <div class="foot-h" style="left:549px">Liens Rapides</div>
  <nav class="foot-links">
    <a class="active" style="top:73px">Maison</a>
    <a style="top:103px">Compétences</a>
    <a style="top:134px">Présentation</a>
    <a style="top:165px">Contactez-nous</a>
  </nav>
  <div class="foot-h" style="left:830px">Détails Du Contact</div>
  <div class="contact-item" style="top:75px">
    <span class="ic"><svg width="16" height="16" viewBox="0 0 16 16" fill="none" stroke="#fff" stroke-width="1.5"><path d="M8 15s5-5 5-9A5 5 0 0 0 3 6c0 4 5 9 5 9z"/><circle cx="8" cy="6" r="2"/></svg></span>
    <div>45, rue des Forges,<br>Ville, État XY 654321</div>
  </div>
  <div class="contact-item" style="top:125px">
    <span class="ic"><svg width="16" height="16" viewBox="0 0 16 16" fill="none" stroke="#fff" stroke-width="1.5"><path d="M3 2h3l1 4-2 1a8 8 0 0 0 4 4l1-2 4 1v3a1 1 0 0 1-1 1A12 12 0 0 1 2 3a1 1 0 0 1 1-1z"/></svg></span>
    <div><b>Téléphone</b><br>+123-555-0142</div>
  </div>
  <div class="contact-item" style="top:175px">
    <span class="ic"><svg width="16" height="16" viewBox="0 0 16 16" fill="none" stroke="#fff" stroke-width="1.5"><rect x="2" y="4" width="12" height="9"/><path d="M2 4l6 5 6-5"/></svg></span>
    <div><b>E-mail</b><br>info@ferravolt.com</div>
  </div>
  <div class="foot-rule"></div>
  <div class="copyright">© 2023 Ferravolt SA.&nbsp; Tous Droits Réservés</div>
</footer>

</body>
</html>
```